Neues Erscheinungsbild für Veranstaltungsreihe gesucht
Auch über das Projekt hinaus ist Torben schon längere Zeit für uns tätig. Vielen Dank! :-)
Zielgruppe
Wir sind ein kleines Unternehmen, das Events in verschiedenen Städten Deutschlands plant und durchführt. Spezialisiert sind wir auf die Event-Reihe 'Wolkenspiel', bei denen drei Pyrotechniker gegeneinander antreten und in einem Wettstreit um das beste musiksynchrone Feuerwerk um den Sieg kämpfen. Bevor diese den Himmel erleuchten, rundet ein Rahmenprogramm bestehend aus Live-Bands, Feuerspucker-Shows, Kinder-Animation und einem großen kulinarischen Angebot den Abend ab.
Besuchen Sie die Website oder die Facebook-Seite (https://www.sozialnetzbeispiel.de/seiten/Wolkenspiel/582913740265118), um sich ein Bild von der Veranstaltung zu machen.
Aufgabenstellung
Für die oben angesprochene Veranstaltungsreihe mit dem Namen 'Wolkenspiel' benötigen wir ein neues Plakatdesign.
Die Plakate soll auffallen, gut lesbar sein und ins Auge springen, aber dennoch nicht billig aussehen. Beim Betrachten soll direkt klar werden, dass es um Feuerwerk geht.
Auch bei längerer Sonneneinstrahlung auf die Plakate und dem damit einhergehenden Ausbleichen soll der Kontrast der Schrift noch groß sein.
Dieses Projekt ist ein Versuch, nach dessen Ablauf es nicht bei dem Gestalten des Plakates bleibt.
Wenn uns ein Design gefällt, benötigen wir darüber hinaus an andere Formate (A2, 18/1 Plakatwand, 3x2m Plakatwand) angepasste Plakate, ggfs. davon abgeleitete Flyer A6, von den Plakatwänden abgeleitete Banner 4x1m sowie von den Plakaten abgeleitetes Profilfoto und ein Timeline-Foto für Facebook.
Desweiteren benötigen wir eine neue Homepage mit CMS (WordPress, Joomla, Typo3, etc.), sodass Infos, Bilder, Videos und auch neue Veranstaltungen im nächsten Jahr selbst eingepflegt werden können.
Diese Folgeaufträge würden wir dann direkt vergeben.

```html
<!DOCTYPE html>
<html lang="de">
<head>
<meta charset="utf-8">
<title>Wolkenspiel – Der grosse Wettstreit der Pyrotechniker</title>
<link rel="stylesheet" href="https://fonts.googleapis.com/css2?family=Black+Ops+One&family=Michroma&family=Roboto:wght@400;700&display=swap">
<style>
  :root {
    --night: #050304;
    --gold: #e8b21c;
    --white: #ffffff;
    --silver: #c9c9c9;
    --orange: #e88a1a;
  }
  * { margin: 0; padding: 0; box-sizing: border-box; }
  html, body { width: 896px; height: 1200px; overflow: hidden; background: var(--night); }
  .poster {
    position: relative;
    width: 896px;
    height: 1200px;
    overflow: hidden;
    background: var(--night);
    font-family: "Roboto", Arial, sans-serif;
  }
  .fireworks-scene {
    position: absolute;
    inset: 0;
    background:
      radial-gradient(circle 60px at 420px 400px, rgba(255,240,200,0.9), transparent 100%),
      radial-gradient(ellipse 470px 420px at 430px 330px, rgba(240,150,40,0.75), rgba(200,80,60,0.35) 55%, transparent 80%),
      radial-gradient(ellipse 260px 360px at 700px 380px, rgba(200,60,150,0.35), transparent 75%),
      radial-gradient(ellipse 260px 360px at 140px 420px, rgba(200,80,160,0.3), transparent 75%),
      radial-gradient(circle 150px at 40px 40px, rgba(255,210,90,0.85), transparent 80%),
      radial-gradient(ellipse 300px 280px at 330px 720px, rgba(230,40,50,0.8), rgba(160,20,30,0.4) 55%, transparent 85%),
      radial-gradient(ellipse 180px 260px at 620px 700px, rgba(70,200,70,0.55), transparent 80%),
      radial-gradient(circle 190px at 120px 870px, rgba(240,90,70,0.75), transparent 85%),
      radial-gradient(circle 210px at 800px 860px, rgba(250,170,80,0.75), transparent 85%),
      radial-gradient(ellipse 520px 150px at 448px 1130px, rgba(170,30,20,0.75), transparent 80%),
      radial-gradient(ellipse 600px 600px at 448px 560px, rgba(120,40,30,0.35), transparent 80%),
      var(--night);
  }
  .date-badge {
    position: absolute;
    left: 699px; top: 30px;
    width: 171px; height: 226px;
    border: 2px solid var(--gold);
    background: rgba(0,0,0,0.85);
    text-align: center;
    font-weight: 700;
    line-height: 1;
  }
  .date-badge .day { display: block; color: var(--gold); font-size: 66px; margin-top: 8px; }
  .date-badge .num { display: block; color: var(--white); font-size: 92px; margin-top: 2px; letter-spacing: -3px; }
  .date-badge .month { display: block; color: var(--gold); font-size: 46px; margin-top: 2px; font-weight: 400; }
  .presenter {
    position: absolute;
    left: 104px; width: 556px; top: 247px;
    text-align: center;
    font-family: "Michroma", sans-serif;
    font-size: 15px;
    letter-spacing: 1px;
    color: var(--silver);
    text-transform: uppercase;
    white-space: nowrap;
  }
  .event-name {
    position: absolute;
    left: 0; width: 896px; top: 312px;
    text-align: center;
    font-family: "Black Ops One", sans-serif;
    font-size: 92px;
    color: var(--gold);
    letter-spacing: 4px;
    text-transform: uppercase;
    line-height: 1;
  }
  .headline {
    position: absolute;
    left: 0; width: 896px; top: 694px;
    text-align: center;
    font-family: "Black Ops One", sans-serif;
    color: var(--gold);
    text-transform: uppercase;
    line-height: 1;
  }
  .headline span { display: block; }
  .headline .l1 { font-size: 80px; letter-spacing: 1px; }
  .headline .l2 { font-size: 84px; margin-top: 16px; letter-spacing: 1px; }
  .headline .l3 { font-size: 66px; margin-top: 26px; }
  .headline .l4 { font-size: 70px; margin-top: 28px; }
  .website {
    position: absolute;
    left: 0; width: 896px; top: 1080px;
    text-align: center;
    font-size: 45px;
    color: var(--orange);
  }
  .social {
    position: absolute;
    left: 0; width: 896px; top: 1146px;
    display: flex; justify-content: center; align-items: center; gap: 14px;
    font-size: 22px;
    color: var(--white);
  }
  .social .mark { width: 20px; height: 20px; background: var(--orange); display: inline-block; }
  .social .gap { width: 14px; }
</style>
</head>
<body>
<main class="poster">
  <div class="fireworks-scene" role="img" aria-label="Nachthimmel voller goldener, roter, pinker und grüner Feuerwerksexplosionen über einem rot beleuchteten Gebäude"></div>

  <div class="date-badge">
    <span class="day">SA</span>
    <span class="num">31</span>
    <span class="month">AUG</span>
  </div>

  <p class="presenter">Nordlicht Events &amp; Kai Brandt presents</p>
  <h1 class="event-name">Wolkenspiel</h1>

  <h2 class="headline">
    <span class="l1">Der Grosse</span>
    <span class="l2">Wettstreit</span>
    <span class="l3">der</span>
    <span class="l4">Pyrotechniker</span>
  </h2>

  <p class="website">www.wolkenspiel-paderborn.de</p>
  <p class="social">
    <span>sozialnetzbeispiel.de/wolkenspiel</span><span class="mark"></span>
    <span class="gap"></span>
    <span>kurznachricht.de/wolkenspiel</span>
  </p>
</main>
</body>
</html>
```